Shopify Design for Back Pain Patch

We need a design for the Shopify-based homepage of the new Vorlixa Spine Pad.

The Vorlixa spine pad absorbs the surface energy produced by your body when you are in pain and redistributes it, reducing your discomfort. It is approximately 5” x 5” in size, with an adhesive backing on one side and a cloth-like exterior that is neutral/light tan in color.

We need a website design that matches our packaging (see attached assets). This includes the blue/orange color scheme and our key messages:

-Natural relief for back pain
-Soothes using your body's natural energy
-Odorless, Gentle, Easy to Use
-Reusable up to 5 days

We are going to be using the Shopify platform for this website, so we'd like the design to be usable with this theme:
http://pliantframe.tovashelf.com/pages/theme-features

We will do all of the coding, but please keep this layout in mind for the design.

Target Market(s)

The Vorlixa Spine Pad is targeted to people suffering from mild to moderate, chronic back pain, but who desire to continue leading active lives.

Industry/Entity Type

Adhesive

Requirements
Must have
• The design needs to have the same look and feel as the packaging for the back patch. Please feel free to use any of the attached assets in your design (doesn't need to be all).
Should not have
• We do not want to see stock photography other than the assets provided.

```html
<!DOCTYPE html>
<html lang="en">
<head>
<meta charset="utf-8">
<title>Vorlixa Spine Pad</title>
<link rel="stylesheet" href="https://fonts.googleapis.com/css2?family=Roboto+Slab:wght@300;400&display=swap">
<style>
:root{
  --blue:#1a72bd;
  --blue-dark:#135f9f;
  --orange:#f7901e;
  --page:#f3f4f6;
  --hero:#cddce3;
  --hero-light:#e6eef2;
  --text:#3b3b3b;
  --band:#dcdfe7;
  --foot:#b3b8c7;
  --white:#ffffff;
}
*{box-sizing:border-box;margin:0;padding:0}
html,body{width:1135px;height:1200px;overflow:hidden}
body{font-family:"Roboto Slab",Georgia,serif;font-weight:300;color:var(--text);
  background:repeating-linear-gradient(135deg,var(--page) 0 3px,#eceef1 3px 5px);position:relative}
.abs{position:absolute}
.header{left:0;top:0;width:1135px;height:94px;background:var(--blue)}
.brand{left:148px;top:18px;color:var(--orange);font-size:34px;font-weight:400;line-height:1}
.brand small{display:block;font-size:15px;margin-left:40px;margin-top:2px}
.top-links{right:148px;top:15px;text-align:right;color:#cfe3f5;font-size:12.5px;line-height:20px}
.top-links b{font-weight:300;color:var(--white)}
.top-links svg{vertical-align:-2px;margin-right:5px}
.nav{left:148px;top:112px;width:839px;height:37px;background:var(--blue);border-radius:6px;display:flex;align-items:center;color:var(--white);font-size:14px;overflow:hidden}
.nav .home{background:var(--orange);height:100%;width:90px;display:flex;align-items:center;justify-content:center}
.nav span{padding:0 12px}
.nav .sep{padding:0 10px;opacity:.8}
.hero{left:0;top:166px;width:1135px;height:339px;background:linear-gradient(90deg,var(--hero-light),var(--hero) 40%,#dde7ec)}
.features{left:148px;top:208px}
.features h2{font-size:23px;font-weight:400;color:var(--blue);margin-bottom:12px}
.features ul{list-style:none;width:236px}
.features li{font-size:15.5px;color:var(--blue);padding:6px 0 6px 22px;position:relative;border-bottom:1px dashed #9bb5c6;line-height:19px}
.features li:last-child{border:none}
.features li::before{content:"";position:absolute;left:3px;top:12px;width:9px;height:9px;border-radius:50%;background:var(--blue)}
.btn{display:inline-flex;align-items:center;justify-content:center;width:89px;height:30px;background:var(--blue);color:var(--white);border-radius:8px;font-size:13px;font-weight:400}
.photo-circle{left:423px;top:177px;width:282px;height:282px;border-radius:50%;background:radial-gradient(circle at 50% 35%,#dceaf6,#8aa8bf 60%,#3d3f48)}
.photo-small{left:657px;top:406px;width:94px;height:94px;border-radius:50%;background:radial-gradient(circle,#d8c6a0,#a58f6a 60%,#4a4d55);border:3px solid var(--white)}
.photo-person{left:751px;top:166px;width:227px;height:339px;background:linear-gradient(180deg,#d9cfc8,#5a5760 45%,#b86b8a 80%,#3a3a40)}
.col{top:543px;width:262px}
.col h3,.sect-title{font-size:17.5px;font-weight:400;color:var(--blue)}
.col .img{margin-top:15px;width:262px;height:140px}
.col p,.welcome p,.testi p{font-size:11px;line-height:15.7px;margin-top:18px}
.col .btn{position:absolute;right:0;top:286px}
.rule{left:148px;top:884px;width:839px;height:1px;background:#d6d8dc}
.welcome{left:148px;top:910px;width:540px}
.welcome .btn{position:absolute;right:-9px;top:121px}
.testi{left:724px;top:910px;width:263px}
.arrows{position:absolute;right:0;top:0;display:flex;gap:10px}
.arrows i{width:20px;height:20px;display:flex;align-items:center;justify-content:center}
.testi .box{margin-top:15px;background:#d6d9e2;height:118px;padding:18px 13px}
.testi .box p{margin:0}
.testi em{font-style:normal;color:var(--blue)}
.band{left:0;top:1089px;width:1135px;height:55px;background:var(--band)}
.info-tab{left:148px;top:1089px;height:55px}
.info-tab span{position:absolute;left:9px;top:17px;color:var(--white);font-size:17px;font-weight:400}
.info-links{left:322px;top:1108px;font-size:11.5px}
.info-links .sep{margin:0 7px}
.cards{left:777px;top:1108px;display:flex;gap:2px}
.cards i{width:33px;height:18px;background:var(--white);border:1px solid #c9ccd4}
.footer{left:0;top:1144px;width:1135px;height:56px;background:var(--foot)}
.copy{left:147px;top:1167px;font-size:11px}
.social{left:887px;top:1160px;display:flex;gap:9px}
.social i{width:27px;height:27px;border-radius:4px;background:var(--blue-dark)}
</style>
</head>
<body>
<div class="abs header"></div>
<div class="abs brand">Vorlixa<small>Spine Pad</small></div>
<div class="abs top-links">
  <div><svg width="12" height="12" viewBox="0 0 12 12"><rect width="12" height="12" rx="2" fill="#8fd0f2"/><path d="M3 3.5c0 3 2.5 5.5 5.5 5.5l.8-1.4-1.6-.8-.7.8c-1-.4-1.7-1.1-2.1-2.1l.8-.7-.8-1.6z" fill="#1a72bd"/></svg>1-800-555-0142</div>
  <div>Home &nbsp;|&nbsp; <b>Shopping Cart</b> &nbsp;|&nbsp; Check Out</div>
  <div>Welcome visitor you can <b>login</b> or <b>create an account.</b></div>
</div>

<nav class="abs nav">
  <span class="home">HOME</span><span>ABOUT US</span><span class="sep">|</span><span>OUR CLIENTS</span><span class="sep">|</span><span>OUR PRODUCT</span><span class="sep">|</span><span>OUR BLOG</span><span class="sep">|</span><span>BUY NOW</span><span class="sep">|</span><span>CONTACT &nbsp;US</span>
</nav>

<section class="abs hero"></section>
<div class="abs features">
  <h2>OUR FEATURES</h2>
  <ul>
    <li>Natural relief for back pain</li>
    <li>Soothes using your body's natural energy</li>
    <li>Odorless, Gentle, Easy to Use</li>
    <li>Reusable up to 5 days</li>
  </ul>
  <div class="btn" style="margin-top:22px">MORE</div>
</div>
<div class="abs photo-circle" role="img" aria-label="Cyclist stretching with a spine pad on his lower back"></div>
<div class="abs photo-person" role="img" aria-label="Woman holding a yoga mat wearing a spine pad"></div>
<div class="abs photo-small" role="img" aria-label="Close-up of the tan spine pad"></div>

<section class="abs col" style="left:148px">
  <h3>OUR CLIENTS</h3>
  <div class="img" role="img" aria-label="Woman with yoga mat wearing the pad" style="background:linear-gradient(90deg,#c9c6c4,#6b5e63 45%,#c0607e 80%,#111 93%)"></div>
  <p>Lorem Ipsum is simply dummy text of the printing and typesetting industry. Lorem Ipsum has been the industry's standard dummy text ever since the 1500s, when an unknown printer took a galley of type and scrambled it to make a type</p>
  <div class="btn">MORE</div>
</section>
<section class="abs col" style="left:436px">
  <h3>OUR PRODUCTS</h3>
  <div class="img" role="img" aria-label="Runner stretching against a post with the pad" style="background:linear-gradient(90deg,#b8b6b0,#7a8a92 40%,#4b4d52 70%,#9a9a98)"></div>
  <p>Lorem Ipsum is simply dummy text of the printing and typesetting industry. Lorem Ipsum has been the industry's standard dummy text ever since the 1500s, when an unknown printer took a galley of type and scrambled it to make a type</p>
  <div class="btn">MORE</div>
</section>
<section class="abs col" style="left:725px">
  <h3>OUR SPECIALITY</h3>
  <div class="img" role="img" aria-label="Cyclist resting by his bike wearing the pad" style="background:linear-gradient(180deg,#cfe0ee,#8ea3b3 50%,#3e4048)"></div>
  <p>Lorem Ipsum is simply dummy text of the printing and typesetting industry. Lorem Ipsum has been the industry's standard dummy text ever since the 1500s, when an unknown printer took a galley of type and scrambled it to make a type</p>
  <div class="btn">MORE</div>
</section>

<div class="abs rule"></div>

<section class="abs welcome">
  <h3 class="sect-title">WELCOME TO VORLIXA BACK PATH</h3>
  <p style="margin-top:12px">Lorem Ipsum is simply dummy text of the printing and typesetting industry. Lorem Ipsum has been the industry's standard dummy text ever since the 1500s, when an unknown printer took a galley of type and scrambled it to make a type specimen book. It has survived not only five centuries, but also the leap into electronic typesetting, remaining essentially unchanged. It was popularised in the 1960s with the release of Letraset sheets containing Lorem Ipsum passages, and more recently with desktop publishing software like Aldus PageMaker including versions of Lorem Ipsum.</p>
  <div class="btn">MORE</div>
</section>

<section class="abs testi">
  <h3 class="sect-title">TESTIMONIALS</h3>
  <div class="arrows">
    <i style="background:var(--orange)"><svg width="8" height="10" viewBox="0 0 8 10"><path d="M6 1 2 5l4 4" stroke="#fff" stroke-width="2" fill="none"/></svg></i>
    <i style="background:var(--blue)"><svg width="8" height="10" viewBox="0 0 8 10"><path d="M2 1l4 4-4 4" stroke="#fff" stroke-width="2" fill="none"/></svg></i>
  </div>
  <div class="box"><p><em>DR.Lorem</em> Ipsum is simply dummy text of the printing and typesetting industry. Lorem Ipsum has been the industry's standard dummy text ever since the type and scrambled it to make a type</p></div>
</section>

<div class="abs band"></div>
<div class="abs info-tab">
  <svg width="155" height="55" viewBox="0 0 155 55"><path d="M0 0h128l27 27.5L128 55H0z" fill="#1a72bd"/></svg>
  <span>INFORMATION</span>
</div>
<div class="abs info-links">About us<span class="sep">|</span>Privecy policy<span class="sep">|</span>Terms and conditions<span class="sep">|</span>Site map<span class="sep">|</span>Contact us</div>
<div class="abs cards" role="img" aria-label="Accepted payment methods"><i></i><i></i><i></i><i></i><i></i><i></i></div>

<div class="abs footer"></div>
<div class="abs copy">2013@ Allright reserved Designed by Northwind Studio</div>
<div class="abs social" role="img" aria-label="Social media links"><i></i><i></i><i style="background:#5fb6d9"></i></div>
</body>
</html>
```